Business Card Design Project

We would need a business name card for our online website business, http://www.plimo.com.sg/. We would need to include our website on the name card as well.

Target Market(s)

Adults and kids in Singapore, mainly expatriates

Industry/Entity Type

Business

Font styles to use
Sans Serif

Colors

Designer to choose colors to be used in the design.

Requirements
Must have
• Must include our "plimo" logo and we would like our name card to be printed on light craft paper material

```html
<!DOCTYPE html>
<html lang="en">
<head>
<meta charset="utf-8">
<title>Plimo Business Cards</title>
<link rel="stylesheet" href="https://fonts.googleapis.com/css2?family=Open+Sans:wght@400;600;700&display=swap">
<style>
  :root {
    --backdrop: #ece8e2;
    --paper: #fbfbfa;
    --navy: #2e3582;
    --red: #d8262c;
    --ink: #2a2a2a;
    --grey: #6b6b6b;
  }
  * { margin: 0; padding: 0; box-sizing: border-box; }
  html, body { width: 1200px; height: 913px; overflow: hidden; }
  body {
    background: var(--backdrop);
    font-family: "Open Sans", Arial, sans-serif;
    position: relative;
  }
  .card {
    position: absolute;
    width: 525px;
    height: 300px;
    background: var(--paper);
    box-shadow: 0 2px 6px rgba(0,0,0,.12), 0 12px 30px rgba(0,0,0,.08);
    overflow: hidden;
  }
  .card--front { left: 60px; top: 150px; }
  .card--back { left: 615px; top: 460px; }

  /* front */
  .front-brand {
    position: absolute; left: 60px; top: 62px;
    display: flex; align-items: center; gap: 22px;
  }
  .brand-dot {
    width: 110px; height: 110px; border-radius: 50%;
    background: var(--navy);
  }
  .brand-name {
    font-weight: 600; color: var(--navy);
    font-size: 44px; letter-spacing: 3px;
  }
  .front-rule {
    position: absolute; height: 1px; background: var(--navy);
  }
  .front-rule--upper { left: 250px; right: 40px; top: 196px; }
  .front-rule--lower { left: 60px; right: 40px; top: 250px; }
  .front-url {
    position: absolute; right: 40px; top: 210px;
    color: var(--red); font-weight: 700; font-size: 16px;
  }

  /* back */
  .back-brand {
    position: absolute; left: 32px; top: 36px;
    display: flex; align-items: center; gap: 16px;
  }
  .back-brand .brand-dot { width: 62px; height: 62px; }
  .back-brand .brand-name { font-size: 30px; font-weight: 400; color: var(--ink); letter-spacing: 2px; }
  .person {
    position: absolute; right: 36px; top: 40px; text-align: right;
  }
  .person-name { color: var(--navy); font-size: 20px; font-weight: 600; }
  .person-title { color: var(--grey); font-size: 10px; }
  .back-rule {
    position: absolute; height: 1px; background: var(--navy);
  }
  .back-rule--top { left: 260px; right: 36px; top: 98px; }
  .back-rule--bottom { left: 32px; right: 260px; top: 196px; }
  .back-url {
    position: absolute; right: 36px; top: 110px;
    color: var(--red); font-weight: 700; font-size: 15px;
  }
  .contacts {
    position: absolute; left: 32px; top: 208px;
    list-style: none; font-size: 14px; color: var(--ink); line-height: 22px;
  }
  .contacts li { display: flex; align-items: center; gap: 12px; }
  .contacts svg { width: 14px; height: 14px; fill: var(--navy); }
  .accent { color: var(--red); }
</style>
</head>
<body>
  <section class="card card--front">
    <div class="front-brand">
      <span class="brand-dot"></span>
      <span class="brand-name">PLIMO</span>
    </div>
    <div class="front-rule front-rule--upper"></div>
    <p class="front-url">www.plimocorp.com</p>
    <div class="front-rule front-rule--lower"></div>
  </section>

  <section class="card card--back">
    <div class="back-brand">
      <span class="brand-dot"></span>
      <span class="brand-name">PLIMO</span>
    </div>
    <div class="person">
      <p class="person-name">Your Long Name</p>
      <p class="person-title">Your Title</p>
    </div>
    <div class="back-rule back-rule--top"></div>
    <p class="back-url">www.plimocorp.com</p>
    <div class="back-rule back-rule--bottom"></div>
    <ul class="contacts">
      <li>
        <svg viewBox="0 0 16 16"><path d="M3 2h3l1 3-2 1a8 8 0 0 0 5 5l1-2 3 1v3c0 1-1 1-1 1A12 12 0 0 1 2 3s0-1 1-1z"/></svg>
        (+65) 6100 2480
      </li>
      <li>
        <svg viewBox="0 0 16 16"><rect x="4" y="1" width="8" height="5"/><rect x="1" y="6" width="14" height="6" rx="1"/><rect x="4" y="10" width="8" height="5"/></svg>
        (+65) 6100 2487
      </li>
      <li>
        <svg viewBox="0 0 16 16"><path d="M1 3h14v10H1z M1 3l7 6 7-6" stroke="#fff" stroke-width="1"/></svg>
        <span>email@<span class="accent">plimocorp</span>.com</span>
      </li>
    </ul>
  </section>
</body>
</html>
```